Create a memorable Stationary for Security Software Company

TalbrenQuay is the worldwide leader in securing the Internet. Making Internet communications and critical data secure, reliable and available everywhere has been and continues to be our ongoing vision. We are committed to staying focused on real customer needs and to developing new and innovative security solutions that redefine the security landscape.

Industry/Entity Type

Internet

Font styles to use
Serif
Sans Serif
Script

Colors
0792cd
33a6d7
85cae6

```html
<!DOCTYPE html>
<html lang="en">
<head>
<meta charset="utf-8">
<title>TalbrenQuay Business Card</title>
<link rel="stylesheet" href="https://fonts.googleapis.com/css2?family=Roboto:wght@400&display=swap">
<style>
  :root {
    --brand-blue: #0792cd;
    --mid-blue: #33a6d7;
    --light-blue: #85cae6;
    --card-white: #ffffff;
    --backdrop: #e8e5e1;
    --text-white: #ffffff;
  }
  html, body {
    margin: 0;
    padding: 0;
    width: 1200px;
    height: 902px;
    overflow: hidden;
    background: var(--backdrop);
  }
  .canvas {
    position: relative;
    width: 1200px;
    height: 902px;
  }
  .business-card {
    position: absolute;
    left: 148px;
    top: 193px;
    width: 903px;
    height: 515px;
    border-radius: 24px;
    overflow: hidden;
    background: var(--card-white);
    box-shadow: 0 6px 24px rgba(0, 0, 0, 0.12);
    font-family: "Roboto", Arial, sans-serif;
  }
  .card-shapes {
    position: absolute;
    inset: 0;
  }
  .contact-panel {
    position: absolute;
    left: 46px;
    top: 0;
    color: var(--text-white);
  }
  .employee-name {
    position: absolute;
    top: 82px;
    left: 0;
    margin: 0;
    font-size: 31px;
    font-weight: 400;
    white-space: nowrap;
  }
  .employee-title {
    position: absolute;
    top: 121px;
    left: 0;
    margin: 0;
    font-size: 23px;
    color: var(--light-blue);
    white-space: nowrap;
  }
  .postal-address {
    position: absolute;
    top: 222px;
    left: 0;
    margin: 0;
    font-style: normal;
    font-size: 23px;
    line-height: 30px;
    white-space: nowrap;
  }
  .contact-list {
    position: absolute;
    top: 306px;
    left: 0;
    margin: 0;
    padding: 0;
    list-style: none;
    font-size: 23px;
    line-height: 30px;
  }
  .contact-item {
    display: flex;
    align-items: center;
    gap: 8px;
    white-space: nowrap;
  }
  .contact-icon {
    width: 24px;
    height: 24px;
    flex: none;
  }
  .website {
    position: absolute;
    top: 405px;
    left: 0;
    margin: 0;
    font-size: 23px;
    color: var(--light-blue);
    white-space: nowrap;
  }
  .brand-name {
    position: absolute;
    left: 500px;
    top: 222px;
    width: 340px;
    margin: 0;
    text-align: center;
    font-size: 44px;
    font-weight: 400;
    color: var(--mid-blue);
  }
</style>
</head>
<body>
<main class="canvas">
  <section class="business-card">
    <svg class="card-shapes" viewBox="0 0 903 515" width="903" height="515" aria-hidden="true">
      <path class="panel-blue" d="M0 0 H447 C370 150 370 365 447 515 H0 Z" fill="var(--brand-blue)"/>
      <path class="accent-crescent" d="M452 0 C382 150 382 365 452 515 C396 365 396 150 452 0 Z" fill="var(--light-blue)"/>
    </svg>

    <div class="contact-panel">
      <h1 class="employee-name">Employee Name</h1>
      <p class="employee-title">President</p>

      <address class="postal-address">
        0000 Youe Address,2nd Ste.<br>
        Ashford Vale, Texas 1234
      </address>

      <ul class="contact-list">
        <li class="contact-item">
          <svg class="contact-icon" viewBox="0 0 24 24" aria-label="Phone">
            <rect width="24" height="24" rx="2" fill="var(--light-blue)"/>
            <path d="M6 9 C6 7 8 6 12 6 C16 6 18 7 18 9 L15.5 10 L15 8.5 H9 L8.5 10 Z" fill="var(--brand-blue)"/>
            <rect x="7" y="11" width="10" height="7" rx="1" fill="var(--brand-blue)"/>
          </svg>
          <span>+000-000-0000</span>
        </li>
        <li class="contact-item">
          <svg class="contact-icon" viewBox="0 0 24 24" aria-label="Fax">
            <rect width="24" height="24" rx="2" fill="var(--light-blue)"/>
            <rect x="8" y="4" width="8" height="6" fill="var(--card-white)"/>
            <rect x="5" y="10" width="14" height="7" rx="1" fill="var(--brand-blue)"/>
            <rect x="8" y="15" width="8" height="5" fill="var(--card-white)"/>
          </svg>
          <span>123 456 7890</span>
        </li>
        <li class="contact-item">
          <svg class="contact-icon" viewBox="0 0 24 24" aria-label="Email">
            <rect width="24" height="24" rx="2" fill="var(--light-blue)"/>
            <rect x="4" y="7" width="16" height="11" fill="none" stroke="var(--card-white)" stroke-width="1.6"/>
            <path d="M4 7 L12 13.5 L20 7 M4 18 L10 12 M20 18 L14 12" fill="none" stroke="var(--card-white)" stroke-width="1.6"/>
          </svg>
          <span>hello@talbrenquay.com</span>
        </li>
      </ul>

      <p class="website">www.talbrenquay.com</p>
    </div>

    <p class="brand-name">TalbrenQuay</p>
  </section>
</main>
</body>
</html>
```